Veteran Reserved Parking Sign 12x18

Brave Hearts Kinship Network is looking to have a new Veteran Reserved Parking Sign designed. Included in the files are our current logo, the rectangle with the name on it. Also included is our Alt Square version that we will often use. There are several other signs that we kind of like as examples, not not asking for exactly like those, we want you to be creative and show us some new ideas. These are full sized parking signs, 12" wide X 18" height.

Target Market(s)

Veterans and Military Friendly Americans

Industry/Entity Type

Veteran Nonprofit

Font styles to use
Other font styles liked:
• Our logo uses the Franklin Heavy Gothic Font but you are not required to use that font in design.

Requirements
Must have
• Our logo needs to be on there and well as BHKN.ORG
Should not have
• CAN NOT Mention Steadfast Soldier Alliance or have black silhouettes similar to their logo. BHKN is NOT the same nonprofit.

```html
<!DOCTYPE html>
<html lang="en">
<head>
<meta charset="utf-8">
<title>Veteran Parking Only Sign</title>
<link rel="stylesheet" href="https://fonts.googleapis.com/css2?family=Alfa+Slab+One&family=Montserrat:wght@700;800&display=swap">
<style>
  :root {
    --backdrop: #e0e0e0;
    --navy: #0d2d63;
    --navy-glow: #252f7e;
    --red: #d0191a;
    --flag-red: #c8153a;
    --flag-deep: #7d0a22;
    --white: #ffffff;
  }
  html, body {
    margin: 0;
    width: 1200px;
    height: 1200px;
    overflow: hidden;
    background: var(--backdrop);
  }
  .parking-sign {
    position: absolute;
    left: 267px;
    top: 79px;
    width: 667px;
    height: 1033px;
  }
  .headline {
    font-family: "Alfa Slab One", serif;
    font-size: 110px;
  }
  .headline-red { fill: var(--red); }
  .headline-white { fill: var(--white); }
  .thanks-line {
    font-family: "Montserrat", sans-serif;
    font-weight: 700;
    fill: var(--white);
  }
  .thanks-main { font-size: 74px; }
  .thanks-sub { font-size: 45px; }
  .brand-name {
    font-family: "Montserrat", sans-serif;
    font-weight: 800;
    font-size: 64px;
    fill: var(--white);
  }
  .brand-full {
    font-family: "Montserrat", sans-serif;
    font-weight: 700;
    font-size: 21px;
    fill: var(--white);
  }
  .brand-web {
    font-family: "Montserrat", sans-serif;
    font-weight: 700;
    font-size: 20px;
    fill: var(--white);
    letter-spacing: 2px;
  }
  .band-red { fill: var(--red); }
  .band-white { fill: var(--white); }
</style>
</head>
<body>
<svg class="parking-sign" viewBox="0 0 667 1033" xmlns="http://www.w3.org/2000/svg">
  <defs>
    <clipPath id="sign-shape">
      <rect width="667" height="1033" rx="67" ry="67"/>
    </clipPath>
    <radialGradient id="field" cx="50%" cy="45%" r="60%">
      <stop offset="0" stop-color="var(--navy-glow)"/>
      <stop offset="1" stop-color="var(--navy)"/>
    </radialGradient>
    <linearGradient id="flag-tone" x1="0" y1="0" x2="1" y2="0.4">
      <stop offset="0" stop-color="var(--flag-red)"/>
      <stop offset="0.5" stop-color="#e8c9cf"/>
      <stop offset="0.75" stop-color="var(--flag-red)"/>
      <stop offset="1" stop-color="var(--flag-deep)"/>
    </linearGradient>
    <filter id="lift" x="-5%" y="-10%" width="110%" height="130%">
      <feDropShadow dx="3" dy="4" stdDeviation="2" flood-color="#000" flood-opacity="0.45"/>
    </filter>
  </defs>

  <g clip-path="url(#sign-shape)">
    <rect class="sign-field" width="667" height="1033" fill="url(#field)"/>

    <path class="flag-banner" role="img" aria-label="Waving American flag across the top of the sign"
          fill="url(#flag-tone)"
          d="M0 0 H667 V60 C560 70 470 130 380 175 C320 205 290 200 262 190 C200 175 120 220 60 245 C35 258 15 265 0 271 Z"/>

    <g class="stripe-band stripe-band-left">
      <rect class="band-red" x="0" y="738" width="83" height="17"/>
      <rect class="band-white" x="0" y="755" width="83" height="20"/>
      <rect class="band-red" x="0" y="775" width="83" height="16"/>
      <rect class="band-white" x="0" y="791" width="83" height="20"/>
      <rect class="band-red" x="0" y="811" width="83" height="17"/>
    </g>
    <g class="stripe-band stripe-band-right">
      <rect class="band-red" x="584" y="738" width="83" height="17"/>
      <rect class="band-white" x="584" y="755" width="83" height="20"/>
      <rect class="band-red" x="584" y="775" width="83" height="16"/>
      <rect class="band-white" x="584" y="791" width="83" height="20"/>
      <rect class="band-red" x="584" y="811" width="83" height="17"/>
    </g>
  </g>

  <g class="headline-group" filter="url(#lift)">
    <text class="headline headline-red" x="30" y="421" textLength="603" lengthAdjust="spacingAndGlyphs">VETERAN</text>
    <text class="headline headline-white" x="63" y="519" textLength="540" lengthAdjust="spacingAndGlyphs">PARKING</text>
    <text class="headline headline-white" x="173" y="621" textLength="324" lengthAdjust="spacingAndGlyphs">ONLY</text>
  </g>

  <text class="thanks-line thanks-main" x="103" y="788" textLength="464" lengthAdjust="spacingAndGlyphs">THANK YOU</text>
  <text class="thanks-line thanks-sub" x="111" y="834" textLength="452" lengthAdjust="spacingAndGlyphs">FOR YOUR SERVICE</text>

  <g class="brand-mark">
    <rect x="172" y="894" width="54" height="54" fill="var(--white)"/>
    <text class="brand-name" x="244" y="946" textLength="250" lengthAdjust="spacingAndGlyphs">BHKN</text>
    <text class="brand-full" x="333.5" y="978" text-anchor="middle" textLength="310" lengthAdjust="spacingAndGlyphs">Brave Hearts Kinship Network</text>
    <text class="brand-web" x="333.5" y="1008" text-anchor="middle">BHKN.ORG</text>
  </g>
</svg>
</body>
</html>
```